TOLV.
RAKESH ENTERTAINMENT & MEDIA
Use specific fonts
any thing which suits with the LOGO provided
Professional
RAKESH MEHTA
MR.
D-47, NORTH PARK-II , GURGAON 122001,HARYANA, INDIA
rakesh@tolv.co.in
www.tolv.co.in
LOG IN THE CENTRE

```html
<!DOCTYPE html>
<html lang="en">
<head>
<meta charset="utf-8">
<title>TOLV. Business Card</title>
<link href="https://fonts.googleapis.com/css2?family=Open+Sans:wght@400;600;700;800&display=swap" rel="stylesheet">
<style>
  :root {
    --bg: #e9e6e2;
    --card: #ffffff;
    --navy: #1b3f73;
    --blue: #1f6fa6;
    --blue-light: #3b94c6;
    --ink: #3a3a3a;
    --muted: #5c5c5c;
    --rule: #b9b9b9;
    --swoosh-line: #1a1a1a;
  }
  * { margin: 0; padding: 0; box-sizing: border-box; }
  html, body { width: 1200px; height: 852px; overflow: hidden; }
  body {
    background: var(--bg);
    font-family: "Open Sans", Arial, sans-serif;
    position: relative;
  }
  .card {
    position: absolute;
    width: 560px;
    height: 320px;
    background: var(--card);
    border-radius: 18px;
    overflow: hidden;
    box-shadow: 0 6px 18px rgba(0,0,0,0.18);
  }
  .card--front { left: 90px; top: 80px; }
  .card--back { left: 550px; top: 452px; }
  .card__decor { position: absolute; inset: 0; width: 100%; height: 100%; }

  .brand {
    position: absolute;
    display: flex;
    align-items: center;
    gap: 12px;
    color: var(--navy);
    font-weight: 800;
    letter-spacing: 1px;
    line-height: 1;
    white-space: nowrap;
  }
  .brand__dot { width: 18px; height: 18px; background: var(--blue); border-radius: 50%; flex: none; }
  .card--front .brand { left: 50px; top: 140px; font-size: 54px; }
  .card--back .brand { left: 150px; top: 66px; font-size: 76px; }
  .card--back .brand__dot { width: 24px; height: 24px; }

  .name {
    position: absolute;
    color: var(--blue);
    font-weight: 700;
    font-size: 17px;
    line-height: 1.2;
    white-space: nowrap;
  }
  .address {
    position: absolute;
    color: var(--muted);
    font-size: 13px;
    line-height: 1.45;
    white-space: nowrap;
  }
  .divider { position: absolute; width: 1px; background: var(--rule); }

  .card--front .name { left: 268px; top: 26px; }
  .card--front .divider { left: 258px; top: 52px; height: 222px; }
  .card--front .address { left: 276px; top: 72px; }
  .card--front .contacts { left: 276px; top: 158px; }

  .card--back .name { left: 72px; top: 204px; }
  .card--back .address { left: 72px; top: 230px; }
  .card--back .divider { left: 296px; top: 186px; height: 104px; }
  .card--back .contacts { left: 306px; top: 186px; }

  .contacts {
    position: absolute;
    list-style: none;
    color: var(--ink);
    font-size: 13px;
    white-space: nowrap;
  }
  .contacts li { display: flex; align-items: center; gap: 8px; height: 21px; }
  .contacts svg { width: 13px; height: 13px; fill: var(--blue); flex: none; }
</style>
</head>
<body>

<svg width="0" height="0" style="position:absolute">
  <defs>
    <linearGradient id="swooshFill" x1="0" y1="0" x2="1" y2="1">
      <stop offset="0" stop-color="#3b94c6"/>
      <stop offset="1" stop-color="#134d80"/>
    </linearGradient>
    <symbol id="icon-phone" viewBox="0 0 16 16"><path d="M3 1c1 0 2 3 2 4s-1 1-1 2 3 4 4 4 1-1 2-1 4 1 4 2-2 3-3 3C7 15 1 9 1 4c0-1 1-3 2-3z"/></symbol>
    <symbol id="icon-mobile" viewBox="0 0 16 16"><path d="M4 0h8a1 1 0 0 1 1 1v14a1 1 0 0 1-1 1H4a1 1 0 0 1-1-1V1a1 1 0 0 1 1-1zm1 2v10h6V2z"/></symbol>
    <symbol id="icon-fax" viewBox="0 0 16 16"><path d="M4 0h8v5H4zM1 6h14v7h-3v3H4v-3H1zm4 5v3h6v-3z"/></symbol>
    <symbol id="icon-mail" viewBox="0 0 16 16"><circle cx="8" cy="8" r="8"/><path d="M4 5h8v6H4z" fill="#fff"/><path d="M4 5l4 3 4-3" fill="none" stroke="#1f6fa6"/></symbol>
    <symbol id="icon-web" viewBox="0 0 16 16"><circle cx="8" cy="8" r="7" fill="none" stroke="#1f6fa6" stroke-width="2"/><path d="M1 8h14M8 1c-3 4-3 10 0 14M8 1c3 4 3 10 0 14" fill="none" stroke="#1f6fa6"/></symbol>
  </defs>
</svg>

<section class="card card--front" aria-label="Card front">
  <svg class="card__decor" viewBox="0 0 560 320" aria-hidden="true">
    <path d="M410 0H560V120C545 60 490 18 410 0Z" fill="url(#swooshFill)"/>
    <path d="M372 0C470 18 545 70 560 160" fill="none" stroke="var(--swoosh-line)" stroke-width="2"/>
    <path d="M0 190C30 260 100 305 190 320H0Z" fill="url(#swooshFill)"/>
    <path d="M0 150C25 250 110 305 220 320" fill="none" stroke="var(--swoosh-line)" stroke-width="2"/>
  </svg>
  <div class="brand"><span class="brand__dot"></span>TOLV</div>
  <h2 class="name">RAKESH MEHTA</h2>
  <div class="divider"></div>
  <p class="address">D-47, North Park-II ,<br>Sunderpur 140512,<br>Eastland, India</p>
  <ul class="contacts">
    <li><svg><use href="#icon-phone"/></svg>+91-124-5550182</li>
    <li><svg><use href="#icon-mobile"/></svg>+91-9876500321</li>
    <li><svg><use href="#icon-fax"/></svg>+91-124-5550194</li>
    <li><svg><use href="#icon-mail"/></svg>rakesh@tolv.co.in</li>
    <li><svg><use href="#icon-web"/></svg>www.tolv.co.in</li>
  </ul>
</section>

<section class="card card--back" aria-label="Card back">
  <svg class="card__decor" viewBox="0 0 560 320" aria-hidden="true">
    <path d="M400 0H560V110C540 55 480 15 400 0Z" fill="url(#swooshFill)"/>
    <path d="M360 0C460 15 540 65 560 150" fill="none" stroke="var(--swoosh-line)" stroke-width="2"/>
    <path d="M0 230C20 280 60 310 110 320H0Z" fill="url(#swooshFill)"/>
    <path d="M0 200C20 270 80 310 150 320" fill="none" stroke="var(--swoosh-line)" stroke-width="2"/>
  </svg>
  <div class="brand"><span class="brand__dot"></span>TOLV</div>
  <h2 class="name">RAKESH MEHTA</h2>
  <p class="address">D-47, North Park-II ,<br>Sunderpur 140512,<br>Eastland, India</p>
  <div class="divider"></div>
  <ul class="contacts">
    <li><svg><use href="#icon-phone"/></svg>+91-124-5550182</li>
    <li><svg><use href="#icon-mobile"/></svg>+91-9876500321</li>
    <li><svg><use href="#icon-fax"/></svg>+91-124-5550194</li>
    <li><svg><use href="#icon-mail"/></svg>rakesh@tolv.co.in</li>
    <li><svg><use href="#icon-web"/></svg>www.tolv.co.in</li>
  </ul>
</section>

</body>
</html>
```